Lumen Heat Flow Studio – Corporate Brand Identity

We are in need of a full company image and brand identity design for a brand new hot yoga studio in a small but busy and wealthy oil town.
Our logo was designed through artfolkhub and we currently have an open wordpress project in artfolkhub with a deadline of July 14. We plan on continuing to build our marketing presence through artfolkhub or one on one with designers that have been able to capture our vision easily. So, there are many more opportunities for continued projects.
We love our current logo and would like it to be utilized well. We want our logo to be familiar, known and synonymous with hot yoga in Alberta, Canada. We have intentions of opening up more locations and are looking for a strong brand that we can eventually franchise.
We need to display a strong but serene image that demands awe and communicates to people that Lumen Heat Flow is the real deal and will provide them with exactly what they need. Our studio is the perfect balance of what you would gain from going to a gym and developing your physical fitness and visiting a spa and nurturing a quiet mind, calm spirit and finding relaxation. We are all of this in one place. Breathe. Bend. Beam. – Steady Frame. Still Thought. Soft Heart.
In every detail our brand image should feel that “we are it.. the real deal when it comes to yoga…the place you want to be… the community you want to be apart of”. We need to appeal to men and women and a very important part of our business will be offering corporate packages and workplace yoga to the large oil companies in town. Our clientele is affluent so although we want creativity it still needs to be posh and upscale.
Most importantly, we are looking for something that is extraordinarily creative and show stopping. We want to set ourselves apart from all other studios in Canada, in terms of our creative, beautiful print marketing. When I say innovative, I’m thinking outside the box as in we want to be known for having beautiful and creative brand image http://www.quirkmole.com/fitness-and-yoga-ads/ I also like the idea of utilizing an image of the most beautiful oasis – see http://markvaultstudio.com/prana-loft-geneva/
We are in need of at least the following:
- Business Cards – Front & Back
- Standard Letterhead (Size A4)
- Continuation Letterhead
- Envelopes (Sizes C4 & A4, , C5, DL)
- Postcard (for voucher, birthday, marketing)
- Loyalty Card design (front and back) for 10 visits
- Gift Certificate design
- Presentation Folder (for corporate packages)
- Standard Invoice A4 (word template)
- With Compliments Slips A5 (word template)
- Email Signature
OPTIONAL
- Labels for Branded Retail Products (Mat Spray, Room Spray, Aromatherapy)
- Social Media (Facebook Cover, etc)
All items must be editable in regards to changing names, addresses, etc. and high resolution please.
Please let me know if you require the logo in another format - ie. "ai, eps"

```html
<!DOCTYPE html>
<html lang="en">
<head>
<meta charset="utf-8">
<title>Lumen Heat Flow Studio – Stationery</title>
<link href="https://fonts.googleapis.com/css2?family=Marcellus&family=Open+Sans:ital,wght@0,400;0,600;1,400&display=swap" rel="stylesheet">
<style>
  :root{
    --bg:#e8e8e8;
    --paper:#ffffff;
    --teal:#2f8580;
    --teal-soft:#8cc3bf;
    --ink:#3c3c3c;
    --ink-soft:#777777;
    --folder-top:#3e3e3e;
    --folder-bottom:#262626;
    --edge:#d6d6d6;
  }
  *{box-sizing:border-box;margin:0;padding:0}
  html,body{width:1200px;height:859px;overflow:hidden;background:var(--bg)}
  .canvas{position:relative;width:1200px;height:859px;background:var(--bg);font-family:"Open Sans",Arial,sans-serif;color:var(--ink)}
  .sheet{position:absolute;background:var(--paper);box-shadow:0 2px 6px rgba(0,0,0,.12);border:1px solid var(--edge)}

  .wordmark{display:flex;align-items:center;gap:8px;font-family:"Marcellus",Georgia,serif;color:var(--teal);letter-spacing:.12em;text-transform:uppercase;white-space:nowrap}
  .wordmark .dot{width:10px;height:10px;border-radius:50%;background:var(--teal);flex:none}

  /* letterhead */
  .letterhead{left:40px;top:40px;width:380px;height:537px;padding:30px 32px}
  .letterhead .head{display:flex;align-items:center;gap:10px}
  .letterhead .wordmark{font-size:13px}
  .letterhead .head-rule{flex:1;height:1px;background:var(--teal-soft)}
  .letterhead .sender{position:absolute;right:32px;top:56px;text-align:right;font-size:6px;line-height:1.5;color:var(--ink-soft)}
  .letter{margin-top:36px;font-size:7px;line-height:1.6;color:var(--ink)}
  .letter p{margin-bottom:8px}
  .letter .closing{font-style:italic}
  .letterhead .foot-rule{position:absolute;left:32px;right:32px;bottom:26px;height:1px;background:var(--teal-soft)}

  /* folder */
  .folder{left:450px;top:40px;width:380px;height:537px;background:linear-gradient(160deg,var(--folder-top),var(--folder-bottom));border:none}
  .folder .wordmark{position:absolute;left:30px;bottom:74px;font-size:20px;color:var(--teal-soft)}
  .folder .wordmark .dot{background:var(--teal-soft);width:14px;height:14px}
  .folder .folder-rule{position:absolute;left:30px;right:0;bottom:60px;height:1px;background:var(--teal)}

  /* business cards */
  .card{width:280px;height:160px}
  .card-front{left:880px;top:40px;display:flex;align-items:center;justify-content:center}
  .card-front .wordmark{font-size:12px}
  .card-back{left:880px;top:220px;display:flex;align-items:center;padding:0 22px;gap:14px}
  .card-back .wordmark{font-size:9px;flex-direction:column;gap:6px;text-align:center;white-space:normal;width:78px;line-height:1.4}
  .card-back .divider{width:1px;height:80px;background:var(--teal-soft)}
  .card-back .contact{font-size:8px;line-height:1.7;color:var(--teal)}
  .card-back .contact .name{font-weight:600;font-size:9px}

  /* envelope */
  .envelope{left:40px;top:610px;width:400px;height:200px;overflow:hidden}
  .envelope svg.flap{position:absolute;left:0;top:0;width:100%;height:70px}
  .envelope .wordmark{position:absolute;left:0;right:0;top:34px;justify-content:center;font-size:11px}

  /* compliments slip */
  .slip{left:470px;top:610px;width:400px;height:200px;padding:24px 26px}
  .slip .head{display:flex;align-items:center;gap:10px}
  .slip .wordmark{font-size:11px}
  .slip .head-rule{flex:1;height:1px;background:var(--teal-soft)}
  .slip .foot-rule{position:absolute;left:26px;right:26px;bottom:20px;height:1px;background:var(--teal-soft)}
</style>
</head>
<body>
<div class="canvas">

  <section class="sheet letterhead" aria-label="Letterhead">
    <div class="head">
      <div class="wordmark"><span class="dot"></span>Lumen Heat Flow Studio</div>
      <div class="head-rule"></div>
    </div>
    <div class="sender">220 Cedar Bend Road, Fort Alder AB<br>T (780) 555-0142 hello@lumenheatflow.ca</div>
    <div class="letter">
      <p>220 Cedar Bend Road<br>Fort Alder, AB T9H 0K1</p>
      <p>January 20th, 2013</p>
      <p>Mr. Hollis<br>Director, Harbor Lane Children's Center<br>48 Pine Court, Calgary, AB T2P 1J9</p>
      <p>Dear Mr. Hollis,</p>
      <p>In the first paragraph, you open with a brief introduction of yourself and the reason you are writing today.</p>
      <p>The second paragraph carries the details of the letter and its purpose. Keep it clear and short so that the reader can follow along easily.</p>
      <p>The final paragraph closes the letter and thanks the reader.</p>
      <p class="closing">Sincerely,</p>
      <p class="closing">This is where the signature of the writer goes.</p>
      <p>Nadia Reyes</p>
    </div>
    <div class="foot-rule"></div>
  </section>

  <section class="sheet folder" aria-label="Presentation folder">
    <div class="wordmark"><span class="dot"></span>Lumen Heat Flow Studio</div>
    <div class="folder-rule"></div>
  </section>

  <section class="sheet card card-front" aria-label="Business card front">
    <div class="wordmark"><span class="dot"></span>Lumen Heat Flow Studio</div>
  </section>

  <section class="sheet card card-back" aria-label="Business card back">
    <div class="wordmark"><span class="dot"></span>Lumen Heat Flow Studio</div>
    <div class="divider"></div>
    <div class="contact">
      <div class="name">Nadia Reyes</div>
      <div>Studio Director</div>
      <div>220 Cedar Bend Road</div>
      <div>(780) 555-0142</div>
      <div>hello@lumenheatflow.ca</div>
      <div>www.lumenheatflow.ca</div>
    </div>
  </section>

  <section class="sheet envelope" aria-label="DL envelope">
    <svg class="flap" viewBox="0 0 400 70" preserveAspectRatio="none">
      <path d="M0 0 L400 0 L400 50 L200 70 L0 50 Z" fill="#f6f6f6" stroke="#dcdcdc" stroke-width="1"/>
    </svg>
    <div class="wordmark"><span class="dot"></span>Lumen Heat Flow Studio</div>
  </section>

  <section class="sheet slip" aria-label="With compliments slip">
    <div class="head">
      <div class="wordmark"><span class="dot"></span>Lumen Heat Flow Studio</div>
      <div class="head-rule"></div>
    </div>
    <div class="foot-rule"></div>
  </section>

</div>
</body>
</html>
```